Maple Lodging Hub website, brand new company, that rents rooms out in houses to milleniuls

We have a site right now that is weak as heck! We could use some punching it up. So we want it to be fun and cool, with added items in for social media (just twitter now) and anything else you want to throw at us. We do have a “blog” in there dedicated to events (we throw a lot of them) so want to incorporate that. Also have an existing design for a hand out that we want to use as our launching pad for colors… you can deviate from it a bit though.

Target Market(s)

25-40 year olds transitioning to the city from other places in the country. Millennial are the min group

Industry/Entity Type

Real Estate

Coding

Coded - Design and coding required

Number of Pages Required

5+ page

Font styles to use
Sans Serif

Requirements
Must have
• Fun look, same pages as those uploaded, but not necessarily the look and feel of what we have already.
• Follow the content of our posted site www.MapleLodgingHub.example
• FOOTER
• LOGO | SITEMAP | SOCIAL LINKS | MAIN CTA REMINDER | CONTACT INFO | COPYRIGHT INFO | TERMS AND CONDITIONS
Nice to have
• Use as many of my graphics as loaded, but feel free to use stock photos as well interlaced. Including both people in their 20’s, 30’s, 40’s, having a fun time or of nice houses, inside and out.

```html
<!DOCTYPE html>
<html lang="en">
<head>
<meta charset="utf-8">
<title>Maple Lodging Hub</title>
<link href="https://fonts.googleapis.com/css2?family=Open+Sans:wght@400;600;700;800&display=swap" rel="stylesheet">
<style>
:root{
  --blue:#1e6fc2;
  --blue-dark:#15589e;
  --navy:#1d3a5c;
  --green:#6aa835;
  --orange:#f26b21;
  --ink:#3b4552;
  --muted:#7b8794;
  --light:#f1f3f5;
  --white:#ffffff;
}
*{box-sizing:border-box;margin:0;padding:0}
html,body{width:1200px;height:2704px;overflow:hidden}
body{font-family:"Open Sans",Arial,sans-serif;color:var(--ink);background:var(--white);font-size:13px;line-height:1.55}
ul{list-style:none}
.page{width:1200px;height:2704px;display:flex;flex-direction:column}
.page > *{flex-shrink:0}

/* header */
.site-header{height:80px;display:flex;align-items:center;justify-content:space-between;padding:0 110px 0 120px;position:relative}
.brand{display:flex;align-items:center;gap:10px;font-weight:800;font-size:20px;color:var(--navy);text-transform:uppercase;letter-spacing:.5px}
.brand-dot{width:26px;height:26px;background:var(--blue);border-radius:50%}
.topbar{position:absolute;right:110px;top:10px;display:flex;gap:26px;align-items:center;font-size:11px;color:var(--muted)}
.topbar .follow{display:flex;align-items:center;gap:6px}
.topbar .phone{font-size:20px;font-weight:700;color:var(--blue)}
.social{display:flex;gap:6px}
.social span{width:14px;height:14px;border-radius:50%;background:var(--blue)}
.main-nav{display:flex;gap:4px;margin-top:36px}
.main-nav a{font-size:10px;font-weight:700;color:var(--navy);text-decoration:none;text-transform:uppercase;padding:6px 12px}
.main-nav a.active{background:var(--blue);color:var(--white)}

/* hero */
.hero{height:440px;position:relative;background:linear-gradient(180deg,#a9cdef 0%,#d7e6f2 40%,#9aa28e 75%,#5d7a45 100%)}
.hero-title{position:absolute;left:20px;top:330px;color:var(--white);font-weight:800;font-size:30px;line-height:1.05;text-transform:uppercase;text-shadow:0 2px 6px rgba(0,0,0,.35)}
.hero-band{height:110px;background:var(--blue);position:relative}
.slider{position:absolute;left:0;right:0;top:-40px;display:flex;justify-content:center;align-items:flex-start;gap:40px}
.slide{text-align:center;color:var(--white);font-size:11px}
.slide .thumb{width:84px;height:84px;border-radius:50%;border:4px solid var(--white);background:linear-gradient(135deg,#c7d4df,#7e95a8);margin-bottom:6px}
.slide.current .thumb{width:100px;height:100px;margin-top:-8px}
.slider-arrow{width:26px;height:26px;border-radius:50%;background:var(--white);margin-top:30px;display:flex;align-items:center;justify-content:center}

/* why */
.why{height:450px;padding:36px 0 0;text-align:center;overflow:hidden}
.section-title{font-size:20px;font-weight:800;color:var(--navy);text-transform:uppercase;line-height:1.5}
.title-rule{width:60px;height:3px;background:var(--blue);margin:12px auto 26px}
.features{display:flex;flex-wrap:wrap;justify-content:center;gap:22px 90px;width:960px;margin:0 auto}
.feature{width:260px}
.feature-icon{width:58px;height:58px;margin:0 auto 10px;display:block}
.feature h3{font-size:14px;font-weight:700;color:var(--navy);margin-bottom:6px}
.feature p{font-size:11px;color:var(--muted)}

/* included dark band */
.included{height:390px;background:linear-gradient(160deg,#2a7ccc 0%,#1a5fa8 60%,#154f8e 100%);display:flex;justify-content:center;gap:40px;padding-top:36px}
.included-col{width:440px;color:var(--white)}
.included-col h2{font-size:17px;font-weight:800;text-transform:uppercase;margin-bottom:4px}
.included-col .lead{font-size:11px;opacity:.85;margin-bottom:12px}
.tick-list li{font-size:11px;padding:4px 0 4px 22px;position:relative;border-bottom:1px solid rgba(255,255,255,.15)}
.tick-list li::before{content:"";position:absolute;left:2px;top:8px;width:10px;height:5px;border-left:2px solid var(--green);border-bottom:2px solid var(--green);transform:rotate(-45deg)}

/* testimonial */
.testimonial{height:260px;background:linear-gradient(180deg,#e6e9ec,#cfd4d9);position:relative}
.faces{position:absolute;top:-34px;left:0;right:0;display:flex;justify-content:center;gap:26px;align-items:center}
.faces .avatar{width:66px;height:66px;border-radius:50%;border:3px solid var(--white);background:linear-gradient(135deg,#a7b3bd,#5f7282)}
.faces .avatar.current{width:86px;height:86px;border-color:var(--green)}
.quote-box{position:absolute;left:310px;top:86px;width:580px;background:var(--green);color:var(--white);text-align:center;padding:20px 40px 16px;font-size:15px;line-height:1.45}
.quote-box cite{display:block;font-style:normal;font-weight:700;font-size:11px;margin-top:10px}

/* fit / difference */
.fit{height:340px;display:flex;justify-content:center;gap:60px;padding:36px 0 0;background:var(--light)}
.fit-col{width:420px}
.fit-col h2{font-size:17px;font-weight:800;color:var(--blue);text-transform:uppercase;margin-bottom:4px}
.fit-col .lead{font-size:11px;color:var(--muted);margin-bottom:12px}
.cross-list li{font-size:11px;padding:5px 0 5px 20px;position:relative;color:var(--ink)}
.cross-list li::before{content:"";position:absolute;left:2px;top:11px;width:8px;height:8px;background:var(--blue);border-radius:50%}
.fit-col p{font-size:11px;color:var(--muted);margin-bottom:12px}
.btn{display:inline-block;background:var(--orange);color:var(--white);font-weight:700;font-size:11px;text-transform:uppercase;padding:9px 22px;text-decoration:none}

/* news cards */
.news{height:350px;display:flex;justify-content:center;gap:40px;padding:34px 0 0}
.card{width:300px;text-align:center}
.card-photo{height:150px;border-radius:4px;margin-bottom:16px}
.card h3{font-size:12px;font-weight:800;color:var(--navy);text-transform:uppercase;margin-bottom:8px}
.card p{font-size:11px;color:var(--muted);margin-bottom:14px}
.btn-blue{display:inline-block;background:var(--blue);color:var(--white);font-size:10px;font-weight:700;text-transform:uppercase;padding:7px 18px;text-decoration:none}

/* footer */
.site-footer{height:284px;background:var(--blue);color:var(--white);display:flex;justify-content:center;gap:80px;padding-top:44px}
.site-footer .brand{color:var(--white);font-size:18px}
.site-footer .brand-dot{background:var(--white)}
.footer-col h4{font-size:12px;font-weight:800;text-transform:uppercase;margin-bottom:10px}
.footer-col li,.footer-col p{font-size:11px;opacity:.9;margin-bottom:4px}
.footer-social{display:flex;gap:8px;margin-top:14px}
.footer-social span{width:22px;height:22px;border-radius:50%;background:rgba(255,255,255,.25)}
</style>
</head>
<body>
<div class="page">

<header class="site-header">
  <div class="brand"><span class="brand-dot"></span>Maple Lodging Hub</div>
  <div class="topbar">
    <span class="follow">Follow us <span class="social"><span></span></span></span>
    <span>hello@maplelodginghub.example</span>
    <span class="phone">555.014.2290</span>
  </div>
  <nav class="main-nav">
    <a href="#" class="active">Home</a>
    <a href="#">Our Communities</a>
    <a href="#">Amenities</a>
    <a href="#">Options</a>
    <a href="#">Events</a>
    <a href="#">About Us</a>
    <a href="#">Contact</a>
  </nav>
</header>

<section class="hero" role="img" aria-label="Photo of a large two-storey family house with lawn and trees">
  <h1 class="hero-title">Professional<br>Built Communities</h1>
</section>
<div class="hero-band">
  <div class="slider">
    <span class="slider-arrow"><svg width="10" height="10" viewBox="0 0 10 10"><path d="M7 1 3 5l4 4" stroke="#1e6fc2" stroke-width="2" fill="none"/></svg></span>
    <div class="slide"><div class="thumb" role="img" aria-label="House interior photo"></div>Heading 1</div>
    <div class="slide"><div class="thumb" role="img" aria-label="House exterior photo"></div>Heading 2</div>
    <div class="slide current"><div class="thumb" role="img" aria-label="Living room photo"></div>Heading 3</div>
    <div class="slide"><div class="thumb" role="img" aria-label="Kitchen photo"></div>Heading 4</div>
    <div class="slide"><div class="thumb" role="img" aria-label="Backyard photo"></div>Heading 5</div>
    <span class="slider-arrow"><svg width="10" height="10" viewBox="0 0 10 10"><path d="M3 1l4 4-4 4" stroke="#1e6fc2" stroke-width="2" fill="none"/></svg></span>
  </div>
</div>

<section class="why">
  <h2 class="section-title">Why be a part of our community?</h2>
  <div class="title-rule"></div>
  <div class="features">
    <div class="feature">
      <svg class="feature-icon" viewBox="0 0 58 58"><circle cx="29" cy="29" r="27" fill="none" stroke="#1e6fc2" stroke-width="2"/><path d="M29 16a9 9 0 0 0-5 16v5h10v-5a9 9 0 0 0-5-16zM25 41h8" fill="none" stroke="#1e6fc2" stroke-width="2"/></svg>
      <h3>Inspiration and motivation</h3>
      <p>In shared homes there is always someone doing something inspiring. You will find new energy and plenty of people to push you forward.</p>
    </div>
    <div class="feature">
      <svg class="feature-icon" viewBox="0 0 58 58"><circle cx="29" cy="29" r="27" fill="none" stroke="#1e6fc2" stroke-width="2"/><path d="M17 20h24v16H27l-6 5v-5h-4z" fill="none" stroke="#1e6fc2" stroke-width="2"/></svg>
      <h3>Shared Lessons</h3>
      <p>Learn from housemates who have been where you are now. Swap tips, stories and mistakes with people who get it.</p>
    </div>
    <div class="feature">
      <svg class="feature-icon" viewBox="0 0 58 58"><circle cx="29" cy="29" r="27" fill="none" stroke="#1e6fc2" stroke-width="2"/><circle cx="22" cy="25" r="5" fill="none" stroke="#1e6fc2" stroke-width="2"/><circle cx="36" cy="25" r="5" fill="none" stroke="#1e6fc2" stroke-width="2"/><path d="M14 40c2-6 14-6 16 0M28 40c2-6 14-6 16 0" fill="none" stroke="#1e6fc2" stroke-width="2"/></svg>
      <h3>Contacts</h3>
      <p>New to the city? Your housemates and our events open doors to friends, work leads and a network that grows with you.</p>
    </div>
    <div class="feature">
      <svg class="feature-icon" viewBox="0 0 58 58"><circle cx="29" cy="29" r="27" fill="none" stroke="#1e6fc2" stroke-width="2"/><path d="M18 38l8-8 5 5 9-11M34 24h6v6" fill="none" stroke="#1e6fc2" stroke-width="2"/></svg>
      <h3>Opportunities</h3>
      <p>Successful people are always close by, and when you spend time with them, new chances come your way.</p>
    </div>
    <div class="feature">
      <svg class="feature-icon" viewBox="0 0 58 58"><circle cx="29" cy="29" r="27" fill="none" stroke="#1e6fc2" stroke-width="2"/><circle cx="22" cy="25" r="2" fill="#1e6fc2"/><circle cx="36" cy="25" r="2" fill="#1e6fc2"/><path d="M19 33c4 7 16 7 20 0" fill="none" stroke="#1e6fc2" stroke-width="2"/></svg>
      <h3>Fun</h3>
      <p>We host social events and parties all year long, so living with us always means a good time close to home.</p>
    </div>
  </div>
</section>

<section class="included" role="img" aria-label="Faded photo of a bright shared living space under a blue tint">
  <div class="included-col">
    <h2>Whats included?</h2>
    <p class="lead">We believe in making room rental simple, so almost everything is included.</p>
    <ul class="tick-list">
      <li>High speed Wi-Fi</li>
      <li>All utilities and basic supplies</li>
      <li>Optional furnished rooms</li>
      <li>Fully equipped kitchens</li>
      <li>Weekly cleaning of shared areas</li>
      <li>Flexible lease lengths</li>
      <li>Invitations to all our events</li>
      <li>A friendly community of housemates</li>
      <li>Support from our local team seven days a week</li>
    </ul>
  </div>
  <div class="included-col">
    <h2>Is our community a fit for you?</h2>
    <p class="lead">If most of the points below describe you, we are a GREAT fit.</p>
    <ul class="tick-list">
      <li>I like to make new people</li>
      <li>I'm new to the city</li>
      <li>I enjoy shared spaces</li>
      <li>I want flexibility and less hassle</li>
      <li>I'm open to new ideas</li>
      <li>I like to keep a tidy home</li>
      <li>I'm working hard on my goals</li>
    </ul>
  </div>
</section>

<section class="testimonial" role="img" aria-label="Faded group photo of housemates in a lounge">
  <div class="faces">
    <div class="avatar" role="img" aria-label="Housemate portrait photo"></div>
    <div class="avatar" role="img" aria-label="Housemate portrait photo"></div>
    <div class="avatar" role="img" aria-label="Housemate portrait photo"></div>
    <div class="avatar current" role="img" aria-label="Housemate portrait photo"></div>
    <div class="avatar" role="img" aria-label="Housemate portrait photo"></div>
    <div class="avatar" role="img" aria-label="Housemate portrait photo"></div>
    <div class="avatar" role="img" aria-label="Housemate portrait photo"></div>
  </div>
  <blockquote class="quote-box">
    Being a part of this community is inspiring and motivating! I thought I wanted to live on my own, but the reality is I just didnt
    <cite>FROM KTM</cite>
  </blockquote>
</section>

<section class="fit">
  <div class="fit-col">
    <h2>Whats included?</h2>
    <p class="lead">If the list below describes you, you're we are probably NOT a fit.</p>
    <ul class="cross-list">
      <li>I value peace and quiet most</li>
      <li>I'm tired of people</li>
      <li>I don't share at all</li>
      <li>I'm NOT a tidy person</li>
      <li>I don't like social events</li>
      <li>I rarely keep my word</li>
      <li>I have my stuff all over</li>
    </ul>
  </div>
  <div class="fit-col">
    <h2>Experience the difference</h2>
    <p>Traditional apartments and housing rentals are a thing of the past. We have created an all encompassing living experience that aligns perfectly with your lifestyle and ambitions. Maple Lodging Hub is a home with people, not just a room.</p>
    <p>We invite you to explore our selection of homes and discover the passion we have for providing wonderful experiences.</p>
    <a href="#" class="btn">Contact us</a>
  </div>
</section>

<section class="news">
  <article class="card">
    <div class="card-photo" role="img" aria-label="Photo of housemates at a dinner party" style="background:linear-gradient(135deg,#8a6a4f,#d2a878)"></div>
    <h3>Done with MLH</h3>
    <p>After an exhausting day in the office, the thought of going out with friends is the best thing on your mind.</p>
    <a href="#" class="btn-blue">Read more</a>
  </article>
  <article class="card">
    <div class="card-photo" role="img" aria-label="Photo of a group of friends at a recent event" style="background:linear-gradient(135deg,#5f6f86,#c7b49a)"></div>
    <h3>Most recent events</h3>
    <p>MLH hosts a number of regular events as well as occasional get-togethers. See what is planned near you.</p>
    <a href="#" class="btn-blue">Read more</a>
  </article>
  <article class="card">
    <div class="card-photo" role="img" aria-label="Photo of a newly added house with a porch" style="background:linear-gradient(135deg,#9bbad6,#6b8a5a)"></div>
    <h3>Our latest addition</h3>
    <p>We are constantly searching for new homes. Take a look at the newest house we have added to the family.</p>
    <a href="#" class="btn-blue">Read more</a>
  </article>
</section>

<footer class="site-footer">
  <div class="footer-col">
    <div class="brand"><span class="brand-dot"></span>Maple Lodging Hub</div>
    <div class="footer-social"><span></span><span></span><span></span></div>
  </div>
  <div class="footer-col">
    <h4>Contact us</h4>
    <p>555.014.2290</p>
    <p>hello@maplelodginghub.example</p>
  </div>
  <div class="footer-col">
    <h4>Menu</h4>
    <ul>
      <li>Home | Our Communities | Amenities | Pricing | Events | News | Contact</li>
      <li>Copyright © 2016 All Rights Reserved | Terms and Conditions</li>
    </ul>
  </div>
</footer>

</div>
</body>
</html>
```